Need new Spot UV Business Card design

We are looking for a new business card design incorporating Spot UV in black & white options / versions. See examples files and Tobin Ashgrove Design logo.
You can see our website at www.tobinashgrove.ca. We want something classy but yet modern. We are open to black or black and/or white on white with the spot uv. We are open to portrait or landscape. Size should be standard 3.5" x 2". The front of the card should focus on the logo and name "Tobin Ashgrove" only. Fonts used should be "Open sans" or "PT Sans".

Target Market(s)

Mid to high end

Industry/Entity Type

Business

Contact Information for Business Card

Tobin Velasko
416.382.4417
tobin@tobinashgrove.ca
www.tobinashgrove.ca
4175 Brightwell Blvd. E Suite 308
Mississauga, ON L5T 2K9

Requirements
Must have
• Name & Logo

```html
<!DOCTYPE html>
<html lang="en">
<head>
<meta charset="utf-8">
<title>Tobin Ashgrove Design — Business Card</title>
<link href="https://fonts.googleapis.com/css2?family=Open+Sans:wght@300;400;700&display=swap" rel="stylesheet">
<style>
  :root {
    --stage: #646c70;
    --card-dark: #0c0c0c;
    --card-light: #ffffff;
    --ink: #111111;
    --ink-soft: #4a4a4a;
    --paper-text: #ffffff;
    --pattern-a: #1b1b1b;
    --pattern-b: #060606;
  }
  * { margin: 0; padding: 0; box-sizing: border-box; }
  html, body { width: 1200px; height: 900px; overflow: hidden; }
  body {
    background: var(--stage);
    font-family: "Open Sans", Arial, sans-serif;
    display: flex;
    flex-direction: column;
    align-items: center;
    justify-content: center;
    gap: 60px;
  }
  .card {
    position: relative;
    width: 560px;
    height: 320px;
    overflow: hidden;
    box-shadow: 0 10px 30px rgba(0,0,0,0.35);
  }

  /* Front */
  .card-front { background: var(--card-dark); }
  .front-texture {
    position: absolute; inset: 0;
    background: radial-gradient(ellipse at 50% 50%, var(--pattern-a) 0%, var(--pattern-b) 80%);
  }
  .front-brand {
    position: absolute; inset: 0;
    display: flex; align-items: center; justify-content: center; gap: 18px;
    color: var(--paper-text);
  }
  .brand-square {
    width: 74px; height: 74px;
    border: 5px solid var(--paper-text);
  }
  .brand-name {
    font-weight: 400;
    text-transform: uppercase;
    line-height: 0.95;
    font-size: 52px;
    letter-spacing: 1px;
  }

  /* Back */
  .card-back { background: var(--card-light); color: var(--ink); }
  .back-brand {
    position: absolute; left: 30px; top: 28px;
    display: flex; align-items: center; gap: 10px;
  }
  .back-brand .brand-square { width: 34px; height: 34px; border: 3px solid var(--ink); }
  .back-brand .brand-name { font-size: 22px; color: var(--ink); }
  .contact {
    position: absolute; left: 30px; top: 118px;
    font-size: 11.5px; line-height: 1.45; color: var(--ink-soft);
    list-style: none;
  }
  .contact li { display: flex; align-items: center; gap: 7px; }
  .contact .address { display: block; margin-bottom: 4px; }
  .contact svg { width: 10px; height: 10px; flex: none; }
  .holder {
    position: absolute; right: 48px; top: 218px; text-align: right;
  }
  .holder-name { font-weight: 700; font-size: 15px; color: var(--ink); }
  .holder-role { font-weight: 400; font-size: 12px; color: var(--ink-soft); }
  .corner-square {
    position: absolute; right: 30px; bottom: 24px;
    width: 34px; height: 34px; border: 2px solid var(--ink);
  }
</style>
</head>
<body>
  <section class="card card-front">
    <div class="front-texture" role="img" aria-label="Spot UV repeating pattern of small brand marks across the black card face"></div>
    <div class="front-brand">
      <div class="brand-square"></div>
      <div class="brand-name">Tobin<br>Ashgrove</div>
    </div>
  </section>

  <section class="card card-back">
    <div class="back-brand">
      <div class="brand-square"></div>
      <div class="brand-name">Tobin<br>Ashgrove</div>
    </div>
    <ul class="contact">
      <li class="address">4175 Brightwell Blvd. E Suite 308<br>Mississauga, ON L5T 2K9</li>
      <li>
        <svg viewBox="0 0 10 10" aria-hidden="true"><path d="M2 0.5 L3.6 2.6 L2.8 3.6 Q4 6 6.4 7.2 L7.4 6.4 L9.5 8 L8.4 9.5 Q1 8.6 0.5 1.6 Z" fill="#333"/></svg>
        416.382.4417
      </li>
      <li>
        <svg viewBox="0 0 10 10" aria-hidden="true"><rect x="0.5" y="2" width="9" height="6.5" fill="none" stroke="#333"/><path d="M0.5 2 L5 5.6 L9.5 2" fill="none" stroke="#333"/></svg>
        tobin@tobinashgrove.ca
      </li>
      <li>
        <svg viewBox="0 0 10 10" aria-hidden="true"><circle cx="5" cy="5" r="4.4" fill="none" stroke="#333"/><ellipse cx="5" cy="5" rx="1.9" ry="4.4" fill="none" stroke="#333"/><path d="M0.6 5 H9.4" stroke="#333"/></svg>
        www.tobinashgrove.ca
      </li>
    </ul>
    <div class="holder">
      <div class="holder-name">Tobin Velasko</div>
      <div class="holder-role">Owner</div>
    </div>
    <div class="corner-square"></div>
  </section>
</body>
</html>
```